Tiny Summit Marketing Booklet Design

•To create 2 brochure designs
1st booklet Complex 8.5X11” 20-24 page Brochure booklet targetted at Enterprise clients

2rd booklet 10-12 page Borchure booklet for parents and schools

•Text content, photos and logos to be supplied by customer

We need a product/service brochure that explains our programme “Tiny Summit” managed and run byViva Kids Pte ltd. The designer must clearly outline our vision and mission of this programme

Lumo kids is part of the Lumo Group of Education companies that develop programmes and educational software programme for schools, institutions and its service centers.

Tiny Summit is a Sports and Education programme that is in the business of changing lives through values.
The materials are targeted to be distributed to School Leaders and Parents.

We are looking for a professional look for both brochure booklet with our rebranded logos. The Logos of both the company and the product logo Tiny Summit will be uploaded within the week with further materials to be developed.

For the purposes of this contest and shortlist selection, we require only the 1st 4 pages to be designed.

The corporate colors are Navy Blue and Golden Yellow. Designers are welcome to design creatively with a new look or colours without losing any professionaly look.

Please use the uploaded existing draft in 2 powerpoints to begin your design.

Target Market(s)

School leaders which include Principals and corporate stakeholders

You can view a similar progamme onn TV run by the founder of Tiny Summit at http://clipvault.example/watch/qTrb82Lxm0p

Industry/Entity Type

Software

Requirements
Should not have
• have any playful colours

```html
<!DOCTYPE html>
<html lang="en">
<head>
<meta charset="utf-8">
<title>Tiny Summit – Changing Lives with Values Booklet Covers</title>
<link rel="stylesheet" href="https://fonts.googleapis.com/css2?family=Patrick+Hand+SC&family=Patrick+Hand&display=swap">
<style>
  :root {
    --page-bg: #ece9e4;
    --navy-top: #2c3a98;
    --navy-bottom: #1f2a7c;
    --navy-deep: #232d84;
    --navy-light: #3a4fb0;
    --gold: #f5b21c;
    --gold-deep: #ee9c14;
    --gold-light: #fdd536;
    --title-yellow: #f3e13c;
    --text-gold: #f0c44a;
  }
  * { margin: 0; padding: 0; box-sizing: border-box; }
  html, body {
    width: 1200px;
    height: 900px;
    overflow: hidden;
    background: var(--page-bg);
  }
  .spread {
    position: absolute;
    left: 150px;
    top: 165px;
    display: flex;
    gap: 20px;
  }
  .cover {
    position: relative;
    width: 440px;
    height: 570px;
    overflow: hidden;
    background: linear-gradient(160deg, var(--navy-top), var(--navy-bottom));
    font-family: "Patrick Hand SC", "Patrick Hand", cursive;
    color: var(--title-yellow);
  }
  .brand {
    position: absolute;
    display: flex;
    flex-direction: column;
    align-items: center;
    gap: 4px;
  }
  .brand-mark {
    width: 54px;
    height: 54px;
    background: var(--gold);
  }
  .brand-name {
    font-size: 17px;
    line-height: 1;
    color: var(--title-yellow);
    white-space: nowrap;
  }
  .cover-front .brand { left: 10px; top: 8px; }
  .cover-back .brand { left: 50%; top: 60px; transform: translateX(-50%); }

  .title {
    position: absolute;
    left: 0;
    right: 0;
    top: 100px;
    text-align: center;
    font-weight: 400;
  }
  .title-main {
    display: block;
    font-size: 68px;
    line-height: 1;
    letter-spacing: 1px;
    padding-left: 20px;
  }
  .title-link {
    display: block;
    font-family: "Patrick Hand", cursive;
    font-size: 24px;
    line-height: 1;
    margin-top: 4px;
    padding-left: 10px;
  }
  .title-sub {
    display: block;
    font-size: 48px;
    line-height: 1;
    padding-left: 10px;
  }
  .partner-line {
    position: absolute;
    left: 0;
    right: 0;
    top: 212px;
    text-align: center;
    font-size: 15px;
    letter-spacing: 1px;
    color: var(--text-gold);
  }
  .waves {
    position: absolute;
    left: 0;
    bottom: 0;
    width: 440px;
    height: 240px;
    display: block;
  }
</style>
</head>
<body>
  <main class="spread">
    <section class="cover cover-front">
      <div class="brand">
        <span class="brand-mark"></span>
        <span class="brand-name">Tiny Summit</span>
      </div>
      <h1 class="title">
        <span class="title-main">Changing Lives</span>
        <span class="title-link">with</span>
        <span class="title-sub">Values</span>
      </h1>
      <svg class="waves" viewBox="0 0 440 240" preserveAspectRatio="none" aria-hidden="true">
        <path d="M0 50 C130 5 300 -5 440 35 L440 240 L0 240Z" fill="var(--navy-light)"/>
        <path d="M0 85 C150 35 300 30 440 55 L440 240 L0 240Z" fill="var(--gold-deep)"/>
        <path d="M0 98 C150 55 300 55 440 72 L440 240 L0 240Z" fill="var(--navy-deep)"/>
        <path d="M0 120 C140 85 290 140 440 105 L440 240 L0 240Z" fill="var(--gold)"/>
        <path d="M0 150 C150 118 300 170 440 138 L440 240 L0 240Z" fill="var(--gold-light)"/>
        <path d="M0 185 C150 158 300 205 440 172 L440 240 L0 240Z" fill="var(--navy-deep)"/>
      </svg>
    </section>

    <section class="cover cover-back">
      <div class="brand">
        <span class="brand-mark"></span>
        <span class="brand-name">Tiny Summit</span>
      </div>
      <p class="partner-line">In Partnership with</p>
      <svg class="waves" viewBox="0 0 440 240" preserveAspectRatio="none" aria-hidden="true">
        <g transform="translate(440 0) scale(-1 1)">
          <path d="M0 50 C130 5 300 -5 440 35 L440 240 L0 240Z" fill="var(--navy-light)"/>
          <path d="M0 85 C150 35 300 30 440 55 L440 240 L0 240Z" fill="var(--gold-deep)"/>
          <path d="M0 98 C150 55 300 55 440 72 L440 240 L0 240Z" fill="var(--navy-deep)"/>
          <path d="M0 120 C140 85 290 140 440 105 L440 240 L0 240Z" fill="var(--gold)"/>
          <path d="M0 150 C150 118 300 170 440 138 L440 240 L0 240Z" fill="var(--gold-light)"/>
          <path d="M0 185 C150 158 300 205 440 172 L440 240 L0 240Z" fill="var(--navy-deep)"/>
        </g>
      </svg>
    </section>
  </main>
</body>
</html>
```